Halvercott Orthodontics business card

Using our existing logo (created with ArtFolio), please create a tasteful, contemporary business card. We are father and daughter orthodontists specializing in braces, clarafit, etc to design healthy, beautiful smiles for children, adolescents, and adults. We would like the design to be family-friendly but not childish.
The final design should include all of the information without looking cluttered (I hope! If necessary to achieve an optimal design, please consider making the card double-sided)
Purple, black, silver on a white card
Please include the following information:
Halvercott Orthodontics (logo)
Marguerite L. Halvercott, DMD
Douglas R. Halvercott, DMD

312 Bramblewood Street
North Andover, MA 01899
978.555.0142

847C Quarry Hollow Street
Methuen, MA 01898
978.555.0187

email frontdesk@halvercottortho.example
website www.halvercottortho.example

```html
<!DOCTYPE html>
<html lang="en">
<head>
<meta charset="utf-8">
<title>Halvercott Orthodontics business card</title>
<link rel="stylesheet" href="https://fonts.googleapis.com/css2?family=Roboto:wght@400;500;700&display=swap">
<style>
  :root {
    --backdrop: #7b6565;
    --card-white: #ffffff;
    --brand-purple: #653594;
    --ink: #111111;
  }
  html, body {
    margin: 0;
    padding: 0;
    width: 1200px;
    height: 1200px;
    overflow: hidden;
    background: var(--backdrop);
    font-family: "Roboto", Arial, sans-serif;
  }
  .canvas {
    position: relative;
    width: 1200px;
    height: 1200px;
  }
  .card {
    position: absolute;
    width: 658px;
    height: 375px;
    border-radius: 19px;
    overflow: hidden;
  }
  .card--front {
    left: 122px;
    top: 156px;
    background: var(--card-white);
  }
  .card--back {
    left: 409px;
    top: 684px;
    background: var(--brand-purple);
  }

  .brand {
    position: absolute;
    display: flex;
    align-items: center;
    gap: 8px;
    font-weight: 500;
    white-space: nowrap;
  }
  .brand__dot {
    border-radius: 50%;
    flex: none;
  }
  .card--front .brand {
    left: 22px;
    top: 172px;
    color: var(--brand-purple);
    font-size: 21px;
  }
  .card--front .brand__dot {
    width: 18px;
    height: 18px;
    background: var(--brand-purple);
  }

  .divider {
    position: absolute;
    left: 314px;
    top: 40px;
    width: 3px;
    height: 295px;
    border-radius: 2px;
    background: var(--brand-purple);
  }

  .doctors {
    position: absolute;
    left: 334px;
    top: 46px;
    margin: 0;
    font-size: 19px;
    font-weight: 500;
    line-height: 25px;
    color: var(--ink);
  }
  .doctors__name {
    display: block;
    white-space: nowrap;
  }

  .contact-list {
    position: absolute;
    left: 336px;
    top: 118px;
    margin: 0;
    padding: 0;
    list-style: none;
    color: var(--ink);
  }
  .contact {
    position: relative;
    padding-left: 39px;
    font-weight: 500;
    font-size: 13px;
    line-height: 17px;
    white-space: nowrap;
  }
  .contact__icon {
    position: absolute;
    left: 0;
    width: 22px;
    height: 22px;
    fill: var(--ink);
  }
  .contact--phone { height: 26px; padding-top: 3px; box-sizing: border-box; }
  .contact--phone .contact__icon { top: 0; }
  .contact--address { height: 40px; }
  .contact--address .contact__icon { top: 7px; }
  .contact--email { height: 31px; font-size: 16px; line-height: 20px; padding-top: 1px; }
  .contact--email .contact__icon { top: 0; }
  .contact--web { padding-top: 2px; }
  .contact--web .contact__icon { top: 0; }

  .card--back .brand {
    left: 0;
    right: 0;
    top: 166px;
    justify-content: center;
    gap: 12px;
    color: var(--card-white);
    font-size: 36px;
  }
  .card--back .brand__dot {
    width: 28px;
    height: 28px;
    background: var(--card-white);
  }
  .tagline {
    position: absolute;
    left: 103px;
    bottom: 0;
    margin: 0;
    width: 438px;
    height: 29px;
    border-radius: 14px 14px 0 0;
    background: var(--card-white);
    color: var(--ink);
    font-size: 17px;
    font-weight: 500;
    line-height: 31px;
    text-align: center;
  }
</style>
</head>
<body>
<main class="canvas">

  <section class="card card--front" aria-label="Business card front">
    <div class="brand">
      <span class="brand__dot"></span>
      <span class="brand__name">Halvercott Orthodontics</span>
    </div>

    <div class="divider"></div>

    <h1 class="doctors">
      <span class="doctors__name">Marguerite L. Halvercott, DMD</span>
      <span class="doctors__name">Douglas R. Halvercott, DMD</span>
    </h1>

    <ul class="contact-list">
      <li class="contact contact--phone">
        <svg class="contact__icon" viewBox="0 0 24 24" aria-hidden="true">
          <path d="M6.6 10.8a15.1 15.1 0 0 0 6.6 6.6l2.2-2.2c.3-.3.7-.4 1-.2 1.1.4 2.3.6 3.6.6.6 0 1 .4 1 1V20c0 .6-.4 1-1 1A17 17 0 0 1 3 4c0-.6.4-1 1-1h3.5c.6 0 1 .4 1 1 0 1.3.2 2.5.6 3.6.1.3 0 .7-.2 1z"/>
        </svg>
        978-555-0142
      </li>
      <li class="contact contact--address">
        <svg class="contact__icon" viewBox="0 0 24 24" aria-hidden="true">
          <path d="M12 2 1 12h3v10h6v-6h4v6h6V12h3L19 9.3V4h-3v2.6z"/>
        </svg>
        312 Bramblewood Street, North Andover<br>MA 01899
      </li>
      <li class="contact contact--phone">
        <svg class="contact__icon" viewBox="0 0 24 24" aria-hidden="true">
          <path d="M6.6 10.8a15.1 15.1 0 0 0 6.6 6.6l2.2-2.2c.3-.3.7-.4 1-.2 1.1.4 2.3.6 3.6.6.6 0 1 .4 1 1V20c0 .6-.4 1-1 1A17 17 0 0 1 3 4c0-.6.4-1 1-1h3.5c.6 0 1 .4 1 1 0 1.3.2 2.5.6 3.6.1.3 0 .7-.2 1z"/>
        </svg>
        978-555-0187
      </li>
      <li class="contact contact--address">
        <svg class="contact__icon" viewBox="0 0 24 24" aria-hidden="true">
          <path d="M12 2 1 12h3v10h6v-6h4v6h6V12h3L19 9.3V4h-3v2.6z"/>
        </svg>
        847C Quarry Hollow Street, Methuen<br>MA 01898
      </li>
      <li class="contact contact--email">
        <svg class="contact__icon" viewBox="0 0 24 24" aria-hidden="true">
          <path d="M1 4h22v16H1zm2 2v.4l9 6.6 9-6.6V6zm0 2.9V18h5.6zM21 8.9 15.4 18H21zM9.9 13.8 4.6 18h14.8l-5.3-4.2-2.1 1.6z"/>
        </svg>
        frontdesk@halvercottortho.example
      </li>
      <li class="contact contact--web">
        <svg class="contact__icon" viewBox="0 0 24 24" aria-hidden="true">
          <path d="M12 1a11 11 0 1 0 0 22 11 11 0 0 0 0-22zm-1 2.1V7H7.6C8.4 4.9 9.6 3.5 11 3.1zm2 0c1.4.4 2.6 1.8 3.4 3.9H13zM8.4 3.7A10 10 0 0 0 5.5 7H3.9a9 9 0 0 1 4.5-3.3zm7.2 0A9 9 0 0 1 20.1 7h-1.6a10 10 0 0 0-2.9-3.3zM3.2 9h2.1a17 17 0 0 0-.3 2H3a9 9 0 0 1 .2-2zm4.1 0H11v2H7a15 15 0 0 1 .3-2zM13 9h3.7c.2.6.3 1.3.3 2h-4zm5.7 0h2.1c.1.6.2 1.3.2 2h-2a17 17 0 0 0-.3-2zM3 13h2c0 .7.1 1.4.3 2H3.2a9 9 0 0 1-.2-2zm4 0h4v2H7.3A15 15 0 0 1 7 13zm6 0h4c0 .7-.1 1.4-.3 2H13zm6 0h2a9 9 0 0 1-.2 2h-2.1c.2-.6.3-1.3.3-2zM3.9 17h1.6a10 10 0 0 0 2.9 3.3A9 9 0 0 1 3.9 17zm3.7 0H11v3.9c-1.4-.4-2.6-1.8-3.4-3.9zM13 17h3.4c-.8 2.1-2 3.5-3.4 3.9zm5.5 0h1.6a9 9 0 0 1-4.5 3.3 10 10 0 0 0 2.9-3.3z"/>
        </svg>
        www.halvercottortho.example
      </li>
    </ul>
  </section>

  <section class="card card--back" aria-label="Business card back">
    <div class="brand">
      <span class="brand__dot"></span>
      <span class="brand__name">Halvercott Orthodontics</span>
    </div>
    <p class="tagline">Generations of Smiles, Crafted with Care!</p>
  </section>

</main>
</body>
</html>
```